Healthy Supplement featuring Moringa products

Need 3 business card options for our reps to order from Printwell. Our reps will be ordering from Printwell once we upload them. Attached is our current designs to show what info needs to be on the cards. Our website is www.tqvitality.com
The business cards will be a template for our reps to order from. Most of our reps are Asian & Hispanic. Please look at our website so you can see who we are to get the look and feel what we need.
Target Market(s)
Adults 30 on up. Health oriented people.
Industry/Entity Type
Health And Wellness
Contact Information for Business Card
Name
Title
Phone
Logo
www.tqvitality.com/my/username
Font styles to use
Requirements
Must have
- Please match our website look and colors. A moringa leaf is nice, but am open to something different.
Nice to have
- Healthy looking and warm, not super cold or too modern.
Should not have
- No harsh colors please.

```html
<!DOCTYPE html>
<html lang="en">
<head>
<meta charset="utf-8">
<title>TQ Vitality – Business Card</title>
<link href="https://fonts.googleapis.com/css2?family=Arimo:wght@400;700&display=swap" rel="stylesheet">
<style>
  :root{
    --bg:#e4e6e8;
    --leaf-green:#6aaa3f;
    --leaf-light:#8cc63f;
    --leaf-pale:#9fd15a;
    --orange:#f0a045;
    --orange-text:#f07a1a;
    --ink:#1f1f1f;
    --paper:#ffffff;
  }
  *{margin:0;padding:0;box-sizing:border-box}
  html,body{width:1200px;height:800px;overflow:hidden;background:var(--bg);font-family:"Arimo",Arial,sans-serif}
  .stage{position:relative;width:1200px;height:800px}
  .card{position:absolute;left:300px;width:600px;height:340px;overflow:hidden;box-shadow:0 6px 18px rgba(0,0,0,.18)}
  .card--back{top:40px;background:var(--leaf-green)}
  .card--front{top:420px;background:var(--paper)}
  .back-pattern{position:absolute;inset:0;background:linear-gradient(135deg,#6cae40,#66a73b)}
  .brand{position:absolute;display:flex;align-items:center;gap:10px;font-weight:700;letter-spacing:2px}
  .brand__dot{width:18px;height:18px;border-radius:50%}
  .card--back .brand{left:50%;top:50%;transform:translate(-50%,-50%);color:var(--paper);font-size:40px}
  .card--back .brand__dot{background:var(--paper)}
  .card--front .brand{left:40px;top:92px;color:var(--leaf-green);font-size:34px}
  .card--front .brand__dot{background:var(--leaf-green)}
  .rep{position:absolute;left:318px;top:82px}
  .rep__name{font-weight:700;font-size:22px;color:var(--leaf-light)}
  .rep__title{font-size:14px;color:var(--orange-text);margin-top:2px}
  .contacts{position:absolute;left:318px;top:146px;list-style:none;font-size:14px;color:var(--ink)}
  .contacts li{display:flex;align-items:center;gap:7px;height:20px}
  .contacts svg{width:12px;height:12px;flex:none}
  .waves{position:absolute;left:0;bottom:0;width:600px;height:340px}
</style>
</head>
<body>
<main class="stage">
  <section class="card card--back">
    <div class="back-pattern" role="img" aria-label="Repeating pattern of moringa leaf sprigs in lighter green"></div>
    <div class="brand"><span class="brand__dot"></span>TQ VITALITY</div>
  </section>

  <section class="card card--front">
    <svg class="waves" viewBox="0 0 600 340" aria-hidden="true">
      <path d="M0,262 C170,300 400,292 600,274 L600,282 C400,302 160,318 0,284 Z" fill="var(--orange)"/>
      <path d="M0,290 C160,326 400,306 600,286 L600,340 L0,340 Z" fill="var(--leaf-green)"/>
    </svg>
    <svg class="waves" viewBox="0 0 600 340" role="img" aria-label="Sprig of moringa leaves on the green band">
      <rect x="390" y="292" width="210" height="48" rx="24" fill="var(--leaf-pale)" opacity=".55"/>
    </svg>

    <div class="brand"><span class="brand__dot"></span>TQ VITALITY</div>

    <div class="rep">
      <div class="rep__name">Daniel Reyes</div>
      <div class="rep__title">Representative</div>
    </div>

    <ul class="contacts">
      <li><svg viewBox="0 0 12 12"><path d="M2.5 1 L4.5 1 L5.2 3.4 L4 4.4 C4.6 5.8 6.2 7.4 7.6 8 L8.6 6.8 L11 7.5 L11 9.5 C11 10.3 10.3 11 9.5 11 C5 11 1 7 1 2.5 C1 1.7 1.7 1 2.5 1Z" fill="var(--orange-text)"/></svg>(123) 456-7890</li>
      <li><svg viewBox="0 0 12 12"><rect x="1" y="2.5" width="10" height="7" fill="none" stroke="var(--orange-text)" stroke-width="1.2"/><path d="M1 2.5 L6 6.5 L11 2.5" fill="none" stroke="var(--orange-text)" stroke-width="1.2"/></svg>daniel@tqvitality.com</li>
      <li><svg viewBox="0 0 12 12"><circle cx="6" cy="6" r="5" fill="none" stroke="var(--orange-text)" stroke-width="1.1"/><ellipse cx="6" cy="6" rx="2.2" ry="5" fill="none" stroke="var(--orange-text)" stroke-width="1"/><path d="M1 6 H11" stroke="var(--orange-text)" stroke-width="1"/></svg>www.tqvitality.com/my/username</li>
    </ul>
  </section>
</main>
</body>
</html>
```